Career Counselor in need of a business card design

Hello Creatives! I'm in need of a business card design for a new company based in Georgia, USA called Pathways By Lantern.

Some things that may be helpful in creating your concept(s) include:

My Logo (Included in the Files section): There are three versions, two versions are in the second file. The all gold stacked (vertical) version is my primary logo and then there are two horizontal versions (one is all gold and the other is gold and grey).

My mission: to empower tweens through young adults to realize and actualize their CAREER ASPIRATIONS.
My vision: for tweens through young adults to LIVE LIFE ON PURPOSE and become CONTRIBUTING MEMBERS OF SOCIETY.

Biblical scriptures that support my ‘Why’: Psalms 127: 3-4(NIV) Children are a heritage from the Lord, offspring a reward from him. Like ARROWS in the hands of a warrior are children…. And Proverbs 29:18(JKV) Where there is no VISION, the people perish.

*Words in ALL CAPS are to emphasize what's important to me and may possibly provide you some inspiration (IDK - Have fun with it)!

Target Market(s)

My ideal customers are parents, guardians, and young adults.

Contact Information for Business Card

My name, degrees and credential: Delphine Marlow, M.S., Ed.S., NCC
Title: College and Career Coach and Consultant

Number: 555.318.2907
Address: 2718 Willowmere Avenue., Suite 405, Macon, GA 31299
Email: info@pathwaysbylantern.example
Website: www.pathwaysbylantern.example

My population: TWEENS • TEENS • EMERGING ADULTS
Services offered: One-On-One Sessions • Small Groups • Workshops

Colors

Designer to choose colors to be used in the design.

Requirements
Nice to have
• Either my mission or vision but I will understand if it does not all fit.
• My mission: To empower tweens through young adults to realize and actualize their career aspirations.
• My vision: For tweens through young adults to live life on purpose and become contributing members of society.

```html
<!DOCTYPE html>
<html lang="en">
<head>
<meta charset="utf-8">
<title>Pathways By Lantern – Business Card</title>
<link href="https://fonts.googleapis.com/css2?family=Roboto+Condensed:wght@400&family=Roboto:wght@400&display=swap" rel="stylesheet">
<style>
  :root {
    --backdrop: #2a2a2a;
    --card-white: #ffffff;
    --gold: #d9ad3c;
    --gold-light: #f7d568;
    --gold-deep: #d1a53d;
    --ink-grey: #6f6f6f;
    --ink-dark: #4a4a4a;
    --divider: #d8d8d8;
  }
  * { box-sizing: border-box; margin: 0; padding: 0; }
  html, body {
    width: 1125px; height: 1200px; overflow: hidden;
    background: var(--backdrop);
  }
  .card {
    position: absolute; left: 171px; width: 826px; height: 472px;
    overflow: hidden;
  }
  .card-front { top: 106px; background: var(--card-white); }
  .card-back {
    top: 639px;
    background: linear-gradient(180deg, var(--gold-light) 0%, var(--gold-deep) 100%);
  }

  /* Front */
  .brand-block {
    position: absolute; left: 56px; top: 140px; width: 280px;
    display: flex; flex-direction: column; align-items: center; gap: 16px;
  }
  .brand-dot {
    width: 60px; height: 60px; border-radius: 50%;
    background: var(--gold);
  }
  .brand-name {
    font-family: "Roboto Condensed", sans-serif; font-weight: 400;
    font-size: 30px; color: var(--gold); text-align: center; line-height: 1.1;
  }
  .divider {
    position: absolute; left: 358px; top: 116px; width: 1px; height: 248px;
    background: var(--divider);
  }
  .contact-block { position: absolute; left: 388px; top: 120px; }
  .person-name {
    font-family: "Roboto Condensed", sans-serif; font-size: 30px;
    color: var(--gold); line-height: 1.2; white-space: nowrap;
  }
  .person-name .credentials { font-size: 19px; }
  .person-title {
    font-family: "Roboto Condensed", sans-serif; font-size: 20px;
    color: var(--ink-grey); margin-top: 2px;
  }
  .address {
    font-family: Roboto, sans-serif; font-size: 19px; line-height: 25px;
    color: var(--ink-dark); margin-top: 14px;
  }
  .contact-list { list-style: none; margin-top: 14px; }
  .contact-list li {
    font-family: Roboto, sans-serif; font-size: 19px; line-height: 26px;
    color: var(--ink-dark); display: flex; align-items: center; gap: 10px;
  }
  .contact-list svg { width: 18px; height: 18px; fill: var(--gold); flex: none; }
  .gold-band {
    position: absolute; left: 0; bottom: 0; width: 100%; height: 21px;
    background: linear-gradient(90deg, var(--gold) 0%, #f1cd5f 55%, var(--gold) 100%);
  }

  /* Back */
  .back-mark {
    position: absolute; left: 0; top: 96px; width: 100%;
    display: flex; flex-direction: column; align-items: center; gap: 22px;
  }
  .back-ring {
    width: 150px; height: 150px; border-radius: 50%;
    border: 8px solid var(--card-white);
  }
  .back-name {
    font-family: "Roboto Condensed", sans-serif; font-size: 34px;
    color: var(--card-white);
  }
  .back-details {
    position: absolute; left: 0; top: 354px; width: 100%;
    text-align: center; font-family: Roboto, sans-serif; font-size: 19px;
    color: var(--card-white);
  }
  .services {
    display: inline-block; padding-bottom: 3px;
    border-bottom: 1px solid var(--card-white);
  }
  .population { margin-top: 5px; }
</style>
</head>
<body>
  <section class="card card-front">
    <div class="brand-block">
      <div class="brand-dot"></div>
      <div class="brand-name">Pathways By Lantern</div>
    </div>
    <div class="divider"></div>
    <div class="contact-block">
      <h1 class="person-name">Delphine Marlow, <span class="credentials">M.S., Ed.S., NCC</span></h1>
      <p class="person-title">College &amp; Career Coach &amp; Consultant</p>
      <p class="address">2718 Willowmere Avenue.,<br>Suite 405, Macon, GA 31299</p>
      <ul class="contact-list">
        <li>
          <svg viewBox="0 0 24 24" aria-hidden="true"><path d="M6.6 10.8c1.4 2.8 3.8 5.1 6.6 6.6l2.2-2.2c.3-.3.7-.4 1-.2 1.1.4 2.3.6 3.6.6.6 0 1 .4 1 1V20c0 .6-.4 1-1 1C10.6 21 3 13.4 3 4c0-.6.4-1 1-1h3.5c.6 0 1 .4 1 1 0 1.3.2 2.5.6 3.6.1.3 0 .7-.2 1L6.6 10.8z"/></svg>
          555.318.2907
        </li>
        <li>
          <svg viewBox="0 0 24 24" aria-hidden="true"><path d="M2 6h20v12H2z M2 6l10 7 10-7" fill="var(--gold)"/><path d="M3 7l9 6.3L21 7" fill="none" stroke="#fff" stroke-width="1.5"/></svg>
          info@pathwaysbylantern.example
        </li>
        <li>
          <svg viewBox="0 0 24 24" aria-hidden="true"><circle cx="12" cy="12" r="10"/><path d="M7 6c2 1 3 3 2 5s1 3 2 4-1 3 0 5M14 3c0 2 2 3 4 3M15 12c2 0 4 1 5 3" fill="none" stroke="#fff" stroke-width="1.4"/></svg>
          www.pathwaysbylantern.example
        </li>
      </ul>
    </div>
    <div class="gold-band"></div>
  </section>

  <section class="card card-back">
    <div class="back-mark">
      <div class="back-ring"></div>
      <div class="back-name">Pathways By Lantern</div>
    </div>
    <div class="back-details">
      <p class="services">Services offered: One-On-One Sessions • Small Groups • Workshops</p>
      <p class="population">My population: Tweens • Teens • Merging Adults</p>
    </div>
  </section>
</body>
</html>
```